ZEPHIRO needs a new business card!

ZEPHIRO is a group of gaming enthusiasts who are looking for a new corporate business card.

The typeface should be modern and minimalist with attention paid to spacing between the letters and the letters 'zephiro' look relative to each other.

Should clean, crisp and minimalist - looking serious overall but with slight tweaks to the letters to make them look playful...

Black on white is fine.

Details on the card should include:
-the word 'zephiro'
-a job title (use any, for e.g. founder)
-a name (e.g. Ned Falka)
-phone number
-email address

For inspiration: http://brisket.tumblevane-cdn.example/wp-content/uploads/2013/07/mela-1.jpg

Target Market(s)

Video gaming enthusiasts

Industry/Entity Type

Business

Requirements
Must have
• Black letter on white background.
The word "zephiro"
Nice to have
• Maybe use a conservative font like Gibraltar or Helvetica and tweaking each letter individually.

You can insert normal job titles under the "zephiro" typeface
Should not have
• Should not be cartoony or childish fonts. No colors.

```html
<!DOCTYPE html>
<html lang="en">
<head>
<meta charset="utf-8">
<title>ZEPHIRO Business Card</title>
<link rel="stylesheet" href="https://fonts.googleapis.com/css2?family=Montserrat:wght@400&family=Roboto:ital,wght@1,300&display=swap">
<style>
  :root {
    --paper: #ffffff;
    --ink: #1c1c1c;
    --ink-soft: #555555;
  }
  html, body {
    margin: 0;
    padding: 0;
    overflow: hidden;
    background: var(--paper);
  }
  .card {
    position: relative;
    width: 1200px;
    height: 777px;
    background: var(--paper);
    overflow: hidden;
  }
  .card__lines {
    position: absolute;
    inset: 0;
  }
  .wordmark {
    position: absolute;
    left: 412px;
    top: 342px;
    height: 115px;
    box-sizing: border-box;
    padding: 0 34px 0 50px;
    border: 3px solid var(--ink);
    display: flex;
    align-items: center;
    font-family: "Montserrat", sans-serif;
    font-weight: 400;
    font-size: 50px;
    letter-spacing: 16px;
    color: var(--ink);
  }
  .details {
    position: absolute;
    left: 417px;
    top: 500px;
    font-family: "Roboto", sans-serif;
    font-style: italic;
    font-weight: 300;
    color: var(--ink-soft);
  }
  .details__name {
    margin: 0 0 42px;
    font-size: 36px;
    letter-spacing: 9px;
  }
  .details__role {
    margin-left: 30px;
  }
  .details__contact {
    margin: 0;
    font-size: 31px;
    letter-spacing: 6.5px;
    line-height: 53px;
  }
</style>
</head>
<body>
  <main class="card">
    <svg class="card__lines" width="1200" height="777" viewBox="0 0 1200 777" aria-hidden="true">
      <polyline points="25,0 287,395 375,395" fill="none" stroke="#1c1c1c" stroke-width="3"/>
      <line x1="1032" y1="0" x2="1200" y2="262" stroke="#1c1c1c" stroke-width="3"/>
      <line x1="1062" y1="0" x2="1200" y2="225" stroke="#1c1c1c" stroke-width="3"/>
    </svg>

    <div class="wordmark">ZEPHIRO</div>

    <section class="details">
      <p class="details__name">Ned Falka<span class="details__role">// member</span></p>
      <p class="details__contact">email: ned.falka@zephiro.com<br>phone: +440 987 654</p>
    </section>
  </main>
</body>
</html>
```